Stationery Design Project

I would like professional stationery that will be branded with our logo.

also, I have application- multipage that I would like to brand. I will attach an example of one of the pages.

Perhaps- this could be the same design, but due to spacing, it may be best to do slight variations.

Target Market(s)

The audience is our donors and supporters who have a heart for the disenfranchised. They are mostly professional and often have significant wealth. They do their work with excellence and I want an image that makes them feel confident we know what we are doing. this is why i tend to say i want a professional look. Also, I want the feel to be uplifting, something that is somewhat artistic and classy.

Industry/Entity Type

It Professional

Font styles to use
Serif

Requirements
Must have
• Generally, simple but I do want a stylized look...

512-684-2730
www.brightmorrowfund.org
PO Box 384927 Dallas, TX 75211
admin@brightmorrowfund.org
Nice to have
• i like to use the colors in our logo
Should not have
• hearts and country look

```html
<!DOCTYPE html>
<html lang="en">
<head>
<meta charset="utf-8">
<title>Bright Morrow Letterhead</title>
<link rel="stylesheet" href="https://fonts.googleapis.com/css2?family=Cinzel:wght@700&family=Crimson+Text:ital@0;1&display=swap">
<style>
  :root {
    --paper: #ffffff;
    --ink: #141414;
    --blue-deep: #1f5fae;
    --blue-sky: #4aa6e2;
    --blue-mid: #2b74c4;
    --gold: #f6c61a;
    --wash-blue: #e9ecf7;
    --wash-gold: #fdf6de;
  }
  * { margin: 0; padding: 0; box-sizing: border-box; }
  html, body { width: 848px; height: 1200px; overflow: hidden; background: var(--paper); }
  .letterhead { position: relative; width: 848px; height: 1200px; background: var(--paper); overflow: hidden; }
  .side-rule { position: absolute; left: 0; top: 0; width: 70px; height: 1200px; }
  .backdrop {
    position: absolute; left: 60px; top: 380px; width: 600px; height: 820px;
    background:
      radial-gradient(ellipse 60% 45% at 45% 55%, var(--wash-blue) 0%, rgba(233,236,247,0.6) 55%, rgba(255,255,255,0) 100%),
      radial-gradient(ellipse 50% 30% at 70% 20%, var(--wash-gold) 0%, rgba(255,255,255,0) 100%);
  }
  .brand { position: absolute; left: 158px; top: 82px; display: inline-block; }
  .brand-name {
    font-family: "Cinzel", "Times New Roman", serif; font-weight: 700;
    font-size: 43px; line-height: 1; color: var(--ink); letter-spacing: 0.5px; white-space: nowrap;
  }
  .brand-tagline {
    font-family: "Crimson Text", "Times New Roman", serif; font-style: italic;
    font-size: 20px; line-height: 1; color: var(--ink); text-align: right; margin-top: 8px; white-space: nowrap;
  }
  .contact { position: absolute; left: 74px; top: 1101px; list-style: none; }
  .contact-item {
    display: flex; align-items: center; height: 22.5px;
    font-family: "Crimson Text", "Times New Roman", serif; font-size: 16px; color: var(--ink);
  }
  .contact-icon { width: 13px; height: 13px; margin-right: 5px; fill: var(--blue-deep); }
</style>
</head>
<body>
<main class="letterhead">
  <svg class="side-rule" viewBox="0 0 70 1200" aria-hidden="true">
    <rect x="36" y="0" width="6" height="32" fill="var(--blue-deep)"/>
    <rect x="44" y="0" width="4" height="32" fill="var(--blue-sky)"/>
    <rect x="49" y="0" width="3" height="32" fill="var(--blue-mid)"/>
    <rect x="54" y="0" width="5" height="32" fill="var(--gold)"/>
    <rect x="36" y="183" width="6" height="1017" fill="var(--blue-deep)"/>
    <rect x="44" y="183" width="4" height="1017" fill="var(--blue-sky)"/>
    <rect x="49" y="183" width="3" height="1017" fill="var(--blue-mid)"/>
    <rect x="54" y="183" width="5" height="1017" fill="var(--gold)"/>
  </svg>

  <div class="backdrop" role="img" aria-label="Faint soft background wash in pale blue and gold"></div>

  <header class="brand">
    <div class="brand-name">Bright Morrow</div>
    <div class="brand-tagline">Where brighter days begin</div>
  </header>

  <ul class="contact">
    <li class="contact-item">
      <svg class="contact-icon" viewBox="0 0 16 16" aria-hidden="true"><path d="M3.5 1l2.5 3-1.5 1.8c.9 2 2.6 3.7 4.6 4.6L11 8.9l3 2.5-1.4 2.8C7 14 2 9 1.8 3.4z"/></svg>
      512-684-2730
    </li>
    <li class="contact-item">
      <svg class="contact-icon" viewBox="0 0 16 16" aria-hidden="true"><path d="M8 1a7 7 0 100 14A7 7 0 008 1zm5.4 6.2h-2.5a11 11 0 00-1-4.3 5.5 5.5 0 013.5 4.3zM8 2.6c.7.9 1.3 2.6 1.4 4.6H6.6C6.7 5.2 7.3 3.5 8 2.6zM6.1 2.9a11 11 0 00-1 4.3H2.6a5.5 5.5 0 013.5-4.3zM2.6 8.8h2.5a11 11 0 001 4.3 5.5 5.5 0 01-3.5-4.3zM8 13.4c-.7-.9-1.3-2.6-1.4-4.6h2.8c-.1 2-.7 3.7-1.4 4.6zm1.9-.3a11 11 0 001-4.3h2.5a5.5 5.5 0 01-3.5 4.3z"/></svg>
      www.brightmorrowfund.org
    </li>
    <li class="contact-item">
      <svg class="contact-icon" viewBox="0 0 16 16" aria-hidden="true"><path d="M1 3h14v10H1zm1.6 1.5v.3L8 8.6l5.4-3.8v-.3zm0 2.2v4.8h10.8V6.7L8 10.5z"/></svg>
      admin@brightmorrowfund.org
    </li>
    <li class="contact-item">
      <svg class="contact-icon" viewBox="0 0 16 16" aria-hidden="true"><path d="M8 1.5L1 8h2v6.5h4v-4h2v4h4V8h2z"/></svg>
      PO Box 384927 Austin, TX 78741
    </li>
  </ul>
</main>
</body>
</html>
```